Bellmont Planners, LLC Stationary

Bellmont Planners, LLC is a new financial planning and consulting company. We are looking for designs on business cards, letterhead, envelopes, and anything else that would be useful. Our preference for business card design is two sided. We are looking for a professional and clean look with incorporating the logo and patriotic feel. Thank you to all who participate and good luck!

```html
<!DOCTYPE html>
<html lang="en">
<head>
<meta charset="utf-8">
<title>Bellmont Planners, LLC – Business Card</title>
<link href="https://fonts.googleapis.com/css2?family=Arimo:wght@400;700&display=swap" rel="stylesheet">
<style>
  :root {
    --page-bg: #e9e9ea;
    --navy: #153f6f;
    --flag-red: #c8202a;
    --deep-red: #8e1418;
    --paper: #ffffff;
    --paper-shade: #eeeeee;
    --ink-light: #ffffff;
    --card-w: 700px;
    --card-h: 400px;
  }
  * { box-sizing: border-box; margin: 0; padding: 0; }
  html, body {
    width: 1200px; height: 950px; overflow: hidden;
    background: var(--page-bg);
    font-family: "Arimo", Arial, sans-serif;
  }
  .sheet {
    width: 1200px; height: 950px;
    display: flex; flex-direction: column; align-items: center; justify-content: center;
    gap: 50px;
  }
  .card {
    position: relative;
    width: var(--card-w); height: var(--card-h);
    overflow: hidden;
    box-shadow: 0 10px 28px rgba(0,0,0,.22);
  }

  /* Front */
  .card-front { background: linear-gradient(160deg, var(--paper) 55%, var(--paper-shade) 100%); }
  .front-band { position: absolute; inset: 0; width: 100%; height: 100%; }
  .contact {
    position: absolute; left: 38px; top: 58px;
    color: var(--ink-light);
  }
  .contact-name { font-size: 27px; font-weight: 700; letter-spacing: .3px; }
  .contact-title { font-size: 17px; margin-top: 4px; }
  .contact-address { font-size: 16px; line-height: 1.35; margin-top: 26px; }
  .contact-lines { list-style: none; margin-top: 6px; font-size: 16px; line-height: 1.4; }
  .contact-lines li { display: flex; align-items: center; gap: 9px; }
  .contact-lines svg { width: 15px; height: 15px; flex: none; fill: var(--ink-light); }

  .brand {
    position: absolute; display: flex; align-items: center; gap: 12px;
    font-weight: 700; white-space: nowrap;
  }
  .brand-mark { flex: none; }
  .card-front .brand { left: 376px; top: 160px; color: var(--navy); font-size: 25px; }
  .card-front .brand-mark { width: 26px; height: 26px; background: var(--flag-red); }

  /* Back */
  .card-back { background: linear-gradient(115deg, var(--flag-red) 0%, #b31b22 50%, var(--deep-red) 100%); }
  .card-back .brand {
    left: 50%; top: 160px; transform: translateX(-50%);
    color: var(--ink-light); font-size: 34px;
  }
  .card-back .brand-mark { width: 32px; height: 32px; background: var(--ink-light); }
  .back-web {
    position: absolute; left: 0; right: 0; top: 230px;
    text-align: center; color: var(--ink-light); font-size: 18px; letter-spacing: 2px;
  }
</style>
</head>
<body>
<main class="sheet">

  <section class="card card-front" aria-label="Business card, front">
    <svg class="front-band" viewBox="0 0 700 400" preserveAspectRatio="none" aria-hidden="true">
      <polygon points="0,0 262,0 340,400 0,400" fill="var(--navy)"/>
      <polygon points="270,0 276,0 354,400 348,400" fill="var(--flag-red)"/>
    </svg>

    <div class="contact">
      <p class="contact-name">Daniel Hartwell</p>
      <p class="contact-title">President</p>
      <p class="contact-address">2147 Larkspur Avenue<br>Glen Ridge, NJ 07028</p>
      <ul class="contact-lines">
        <li>
          <svg viewBox="0 0 16 16" aria-label="Phone"><path d="M4 1l3 3-2 2c1 2 3 4 5 5l2-2 3 3-2 3C7 15 1 9 1 3z"/></svg>
          555 0142 7788
        </li>
        <li>
          <svg viewBox="0 0 16 16" aria-label="Fax"><path d="M4 1h8v4H4zM1 6h14v7h-3v2H4v-2H1zM5 11v3h6v-3z"/></svg>
          555 0193 4410
        </li>
        <li>
          <svg viewBox="0 0 16 16" aria-label="Email"><path d="M1 3h14v10H1zM2 4l6 5 6-5v1L8 10 2 5z" fill-rule="evenodd"/></svg>
          daniel@bellmontplanners.com
        </li>
        <li>
          <svg viewBox="0 0 16 16" aria-label="Website"><path d="M8 1a7 7 0 1 0 0 14A7 7 0 0 0 8 1zm0 1.5c1 1.3 1.6 3.3 1.7 5H6.3C6.4 5.8 7 3.8 8 2.5zM6.3 8.5h3.4c-.1 1.7-.7 3.7-1.7 5-1-1.3-1.6-3.3-1.7-5z" fill-rule="evenodd"/></svg>
          www.bellmontplanners.com
        </li>
      </ul>
    </div>

    <div class="brand">
      <span class="brand-mark" aria-hidden="true"></span>
      <span class="brand-name">Bellmont Planners, LLC</span>
    </div>
  </section>

  <section class="card card-back" aria-label="Business card, back">
    <div class="brand">
      <span class="brand-mark" aria-hidden="true"></span>
      <span class="brand-name">Bellmont Planners, LLC</span>
    </div>
    <p class="back-web">www.bellmontplanners.com</p>
  </section>

</main>
</body>
</html>
```